Debt Collection Website Design! We are the solution for landlords to get paid what they are owed.

We are a 3rd party debt collection company that specializes in Residential and Commercial real estate debt collection. We help landlords recover money from past residents by being fair, friendly and aggressive. We also collect/buy/sell/trade civil judgments won resulting from anything from automobile accidents to evictions to a pet zebra getting stolen. We buy single judgments to large portfolios, we also collect judgments for a nominal fee.

I would like a new, modern, easy to navigate website. A spot that we can post news stories or updated information about our company. I have included our company logo that must be on the top of the page. Feel free to ask any questions that will help get the process going.

Target Market(s)

Landlords, small to large apartment complex. Real estate services and lawyers.

Industry/Entity Type

Real Estate

Number of Pages Required

3 page

Requirements
Must have
• Company logo which has been attached. A page where we can explain the collection process, fees and placement. A page where we can explain judgments, collection vs. selling, placement form. I am open to any font/designs and willing to work with anyone.
Nice to have
• Nice to have a spot on the homepage to place news articles about ourselves and our industry.
Should not have
• I don't want it over crowded. Simple, sleek and easy to navigate is best. No gavels on any of the pages. It cannot look legal, say/show anything that we use legal powers to collect. We are not a law office, we don't practice law, we are 3rd party debt collection agency.

```html
<!DOCTYPE html>
<html lang="en">
<head>
<meta charset="utf-8">
<title>Corvane Recovery, LLC</title>
<link href="https://fonts.googleapis.com/css2?family=Open+Sans:wght@300;400;600;700&display=swap" rel="stylesheet">
<style>
:root{
  --navy:#0f2a6b;
  --blue-link:#1b5fa0;
  --text:#3a3a3a;
  --muted:#8a8a8a;
  --band:#f6f6f6;
  --rule:#d9d9d9;
  --footer:#2b2f2e;
  --footer-bottom:#292c2b;
  --white:#ffffff;
}
*{margin:0;padding:0;box-sizing:border-box}
html,body{width:897px;height:1200px;overflow:hidden;background:var(--white)}
body{position:relative;font-family:"Open Sans",Arial,sans-serif;color:var(--text)}
.abs{position:absolute}

.brand{left:74px;top:32px;display:flex;align-items:center;gap:10px}
.brand-mark{width:34px;height:34px;background:var(--navy)}
.brand-name{font-size:19px;font-weight:400;color:var(--navy);line-height:1;letter-spacing:.5px}

.search{left:659px;top:17px;width:164px;height:23px;border:1px solid #d3d3d3;background:#f1f1f1;display:flex}
.search span{flex:1;font-size:8px;color:#666;padding:6px 0 0 10px}
.search i{width:23px;border-left:1px solid #d3d3d3;display:flex;align-items:center;justify-content:center}

.nav{top:63px;left:354px;width:469px;display:flex;justify-content:space-between;font-size:9px;color:#333;letter-spacing:.2px}
.nav a{color:inherit;text-decoration:none;padding:0 4px 9px}
.nav a.active{border-bottom:2px solid var(--navy)}

.hero{left:74px;top:107px;width:749px;height:314px;background:linear-gradient(110deg,#8a7358 0%,#a58a66 35%,#6c7fa6 65%,#2c3b66 100%)}
.hero-arrows{left:108px;top:381px;display:flex;gap:2px}
.hero-arrows span{width:18px;height:18px;background:rgba(60,60,60,.45)}
.hero-shadow{left:130px;top:421px;width:637px;height:12px;background:radial-gradient(ellipse at top,rgba(0,0,0,.12),transparent 70%)}

.welcome{left:74px;top:455px;width:749px;text-align:center}
.welcome h1{font-size:19px;font-weight:700;color:var(--navy);letter-spacing:.3px}
.welcome h2{font-size:14px;font-weight:300;color:#555;margin-top:5px}
.welcome p{font-family:Arial,sans-serif;font-size:8.6px;line-height:20.5px;color:#444;margin-top:8px}

.services{left:0;top:596px;width:897px;height:259px;background:var(--band)}
.section-title{position:absolute;left:0;width:897px;text-align:center;font-size:15px;font-weight:700;color:var(--navy)}
.svc-arrows{left:785px;top:620px;display:flex;gap:2px}
.svc-arrows span{width:18px;height:18px;background:#d9d9d9;display:flex;align-items:center;justify-content:center}
.card{width:228px;top:651px}
.card-photo{height:124px}
.card h3{font-size:9.5px;font-weight:700;color:var(--blue-link);margin-top:13px}
.card p{font-size:8.6px;font-weight:700;color:#555;margin-top:5px;padding-bottom:10px;border-bottom:1px solid var(--rule)}

.news-intro{left:150px;top:910px;width:597px;text-align:center;font-size:9.5px;line-height:15.5px;color:var(--muted)}
.news-item{top:965px;display:flex;gap:10px}
.date{width:47px;height:47px;border-radius:50%;background:var(--navy);color:var(--white);text-align:center;font-size:11.5px;line-height:13px;padding-top:9px;flex:none;border:2px solid #dde3ef}
.news-item h4{font-size:12px;font-weight:400;color:#222;margin-top:1px}
.news-item p{font-size:9.2px;line-height:14px;color:var(--muted);margin-top:4px;padding-left:2px}

.footer{left:0;top:1052px;width:897px;height:90px;background:var(--footer);color:var(--white)}
.fcol{position:absolute;top:28px}
.fcol b{display:block;font-size:10px;font-weight:700}
.fcol .big{font-size:12px;font-weight:600;margin-top:5px}
.fcol .links{font-size:10px;font-style:italic;font-weight:600;text-decoration:underline;margin-top:7px;word-spacing:3px}
.signup{left:592px;top:30px;font-size:10px;font-weight:700;line-height:20px}
.email{left:669px;top:33px;width:154px;height:25px;background:var(--white);display:flex;align-items:center;justify-content:space-between;padding:0 6px 0 7px;font-size:8px;color:#555}
.bottom{left:0;top:1142px;width:897px;height:58px;background:var(--footer-bottom);border-top:1px solid #3a3e3d;color:var(--white)}
.bottom small{position:absolute;left:75px;top:23px;font-size:8px}
.social{position:absolute;left:712px;top:24px;display:flex;gap:12px}
.social span{width:13px;height:13px;border-radius:50%;background:#e8e8e8}
</style>
</head>
<body>

<div class="abs brand"><div class="brand-mark"></div><div class="brand-name">Corvane Recovery, LLC</div></div>

<div class="abs search"><span>Search :</span><i><svg width="10" height="10" viewBox="0 0 10 10"><circle cx="4" cy="4" r="3" fill="none" stroke="#888" stroke-width="1.2"/><line x1="6.2" y1="6.2" x2="9" y2="9" stroke="#888" stroke-width="1.2"/></svg></i></div>

<nav class="abs nav">
  <a class="active" href="#">HOME</a><a href="#">ABOUT US</a><a href="#">SERVICES</a><a href="#">NEWS</a><a href="#">TESTIMONIALS</a><a href="#">CONTACT US</a>
</nav>

<div class="abs hero" role="img" aria-label="Desk scene with a person filling in an application form beside a calculator, glasses and folders"></div>
<div class="abs hero-shadow"></div>
<div class="abs hero-arrows">
  <span><svg width="18" height="18"><path d="M10 6l-3 3 3 3" fill="none" stroke="#ddd"/></svg></span>
  <span><svg width="18" height="18"><path d="M8 6l3 3-3 3" fill="none" stroke="#ddd"/></svg></span>
</div>

<section class="abs welcome">
  <h1>WELCOME TO CORVANE</h1>
  <h2>AT VERO EOS ET&nbsp; ATQUE CORRUPTI QUOS DOLORES ET</h2>
  <p>At vero eos et accusamus et iusto odio dignissimos ducimus qui blanditiis praesentium voluptatum deleniti atque corrupti quos dolores et quas molestias excepturi sint occaecati cupidi-<br>tate non provident, similique sunt in culpa qui officia deserunt mollitia animi, id est laborum et dolorum fuga. Et harum quidem rerum facilis est et expedita distinctio. Nam libero<br>tempore, cum soluta nobis est eligendi optio cumque</p>
</section>

<section class="abs services"></section>
<div class="section-title" style="top:610px">OUR SERVICES</div>
<div class="abs svc-arrows">
  <span><svg width="18" height="18"><path d="M10 6l-3 3 3 3" fill="none" stroke="#fff"/></svg></span>
  <span><svg width="18" height="18"><path d="M8 6l3 3-3 3" fill="none" stroke="#fff"/></svg></span>
</div>

<div class="abs card" style="left:74px">
  <div class="card-photo" role="img" aria-label="Two businessmen in suits reviewing a tablet outside an office tower" style="background:linear-gradient(120deg,#7fa3d0,#3c5478 60%,#1f2a3c)"></div>
  <h3>RESIDENTIAL AND COMMERCIAL</h3>
  <p>LOREM IPSUM IS SIMPLY DUMMY TEXT</p>
</div>
<div class="abs card" style="left:334px">
  <div class="card-photo" role="img" aria-label="Team around a table covered in plans and colour swatches" style="background:linear-gradient(120deg,#b9bfc1,#9aa3a6 50%,#5d6466)"></div>
  <h3>REAL ESTATE DEBT COLLECTION</h3>
  <p>LOREM IPSUM IS SIMPLY DUMMY TEXT</p>
</div>
<div class="abs card" style="left:595px">
  <div class="card-photo" role="img" aria-label="Colleagues meeting around a table in a dark office" style="background:linear-gradient(120deg,#2b3440,#4f5a66 55%,#1b2028)"></div>
  <h3>WE ALSO COLLECT/BUY/SELL/TRADE</h3>
  <p>LOREM IPSUM IS SIMPLY DUMMY TEXT</p>
</div>

<div class="section-title" style="top:879px">LATEST NEWS</div>
<p class="abs news-intro">Sed ut perspiciatis unde omnis iste natus error sit voluptatem accusantium doloremque laudantium, totam rem aperiam, eaque ipsa quae ab illo inventore veritatis et quasi architecto beatae vitae dic</p>

<article class="abs news-item" style="left:73px"><div class="date">24<br>FEB</div><div><h4>At vero eos et accusamus</h4><p>Lorem ipsum dolor sit amet, consecte<br>tuer adipiscing elit, sed diam.</p></div></article>
<article class="abs news-item" style="left:331px"><div class="date">24<br>FEB</div><div><h4>At vero eos et accusamus</h4><p>Lorem ipsum dolor sit amet, consecte<br>tuer adipiscing elit, sed diam.</p></div></article>
<article class="abs news-item" style="left:600px"><div class="date">24<br>FEB</div><div><h4>At vero eos et accusamus</h4><p>Lorem ipsum dolor sit amet, consecte<br>tuer adipiscing elit, sed diam.</p></div></article>

<footer class="abs footer">
  <div class="fcol" style="left:75px"><b>DENMARK</b><div class="big">Cell 11 0000 00001</div></div>
  <div class="fcol" style="left:235px"><b>EMAIL</b><div class="links">Support Newsletter Sales</div></div>
  <div class="fcol" style="left:430px"><b>GERMANY</b><div class="big">Cell 11 0000 00001</div></div>
  <div class="abs signup">SIGN UP<br>NEWSLETTER</div>
  <div class="abs email"><span>Email Address</span><svg width="18" height="11" viewBox="0 0 18 11"><rect x=".5" y=".5" width="17" height="10" fill="#9a9a9a" stroke="#777"/><path d="M.5 .5l8.5 6 8.5-6" fill="none" stroke="#eee"/></svg></div>
</footer>
<div class="abs bottom">
  <small>Copyright © 2015, Corvane. All Rights Reserved.</small>
  <div class="social"><span></span><span></span><span></span><span></span><span></span></div>
</div>

</body>
</html>
```